Web Design Project

We need a web design new company based in Australia. We're a search engine marketing company who predominantly manages Vexora bidlines campaigns.
Currently still deciding on a business name so lets use “Marlow Tappers” for now.
Target market....
small to medium size businesses
- more clicks to their website from the 1st page of Vexora
- more relevant, (higher quality) clicks
- higher return on investment from their bidlines campaign
- more sales, leads, (conversions)
We'd like clean, simple, semi-professional as we'd like to pick up some high end corporate clients.
A website that we love the look and feel of – but they’re a direct competitor so can’t be too similar in design.
http://www.brindlepath.com.au/search-engine-marketing.html
**please check portfolio on this web page..they designs are absolutely stunning!! http://www.brindlepath.com.au/website-design.html
Updates
Please refer to the attached file, a rough sketch of my web page.
place replace...."Afraid your bidlines campaign is underperforming with,....
Industry/Entity Type
Business
Look and feel

```html
<!DOCTYPE html>
<html lang="en">
<head>
<meta charset="utf-8">
<title>Marlow Tappers – Vexora bidlines management</title>
<link rel="stylesheet" href="https://fonts.googleapis.com/css2?family=Francois+One&family=Kalam:wght@400&family=Open+Sans:wght@400;700;800&display=swap">
<style>
  :root {
    --outer-dark: #050708;
    --outer-mid: #1d2326;
    --bar-top: #3a3d40;
    --bar-bottom: #1e2022;
    --teal-light: #2fd0cf;
    --teal: #12a9b0;
    --teal-deep: #07707a;
    --heading-teal: #1b9fb4;
    --orange: #f0581c;
    --orange-deep: #d8430e;
    --gold: #f2c11a;
    --ink: #ffffff;
    --text-grey: #6d6f71;
    --soft-grey: #e6e7e8;
    --paper: #ffffff;
  }
  * { box-sizing: border-box; margin: 0; padding: 0; }
  html, body {
    width: 809px;
    height: 1200px;
    overflow: hidden;
  }
  body {
    background: radial-gradient(ellipse at 50% 30%, var(--outer-mid) 0%, var(--outer-dark) 70%);
    font-family: "Open Sans", Arial, sans-serif;
  }

  .page {
    position: absolute;
    left: 75px;
    top: 0;
    width: 659px;
    height: 1200px;
    background: var(--paper);
  }

  /* ---------- header ---------- */
  .topbar {
    height: 92px;
    background: linear-gradient(var(--bar-top), var(--bar-bottom));
    position: relative;
  }
  .brand {
    position: absolute;
    left: 26px;
    top: 32px;
    display: flex;
    align-items: center;
    gap: 8px;
    font-family: "Francois One", Arial, sans-serif;
    font-size: 22px;
    color: var(--gold);
    text-transform: uppercase;
    letter-spacing: 0.5px;
  }
  .brand-mark {
    width: 18px;
    height: 18px;
    background: var(--gold);
  }
  .phone {
    position: absolute;
    right: 16px;
    top: 10px;
    color: var(--ink);
    font-size: 14px;
    font-weight: 700;
    display: flex;
    align-items: center;
    gap: 6px;
  }
  .main-nav {
    position: absolute;
    right: 12px;
    top: 62px;
    display: flex;
    gap: 16px;
  }
  .main-nav a {
    color: var(--ink);
    text-decoration: none;
    font-size: 12px;
    font-weight: 700;
  }
  .hero {
    height: 328px;
    background: radial-gradient(ellipse at 55% 30%, var(--teal-light) 0%, var(--teal) 45%, var(--teal-deep) 100%);
    position: relative;
  }
  .hero-title {
    position: absolute;
    left: 36px;
    top: 58px;
    width: 420px;
    color: var(--ink);
    font-weight: 800;
    font-size: 30px;
    line-height: 1.22;
  }
  .hero-visual {
    position: absolute;
    right: 36px;
    top: 44px;
    width: 160px;
    height: 180px;
    border-radius: 10px;
    background: linear-gradient(160deg, rgba(230,246,248,0.55), rgba(60,110,130,0.25));
  }

  /* ---------- health check ---------- */
  .health-check {
    height: 420px;
    background: linear-gradient(var(--soft-grey), var(--paper) 70%);
    text-align: center;
    padding-top: 40px;
  }
  .offer {
    display: flex;
    justify-content: center;
    align-items: center;
    gap: 14px;
  }
  .offer-free {
    font-family: "Francois One", Arial, sans-serif;
    font-size: 88px;
    line-height: 1;
    color: var(--orange);
  }
  .offer-name {
    font-family: "Francois One", Arial, sans-serif;
    font-size: 36px;
    line-height: 1.05;
    color: var(--heading-teal);
    text-align: left;
    text-transform: uppercase;
  }
  .step-title {
    font-family: "Kalam", cursive;
    font-size: 28px;
    color: var(--text-grey);
    margin-top: 14px;
  }
  .url-field {
    display: block;
    width: 280px;
    height: 32px;
    margin: 10px auto 0;
    border: 1px solid #c7c9cb;
    background: var(--paper);
    font-family: "Open Sans", Arial, sans-serif;
    font-size: 13px;
    color: #999;
    padding: 0 10px;
  }
  .step-count {
    width: 280px;
    margin: 8px auto 0;
    text-align: right;
    font-size: 12px;
    color: var(--text-grey);
    letter-spacing: 0.5px;
  }
  .next-button {
    display: block;
    width: 96px;
    height: 96px;
    margin: 14px auto 0;
    border: none;
    border-radius: 50%;
    background: radial-gradient(circle at 40% 35%, #f8834a, var(--orange) 55%, var(--orange-deep));
    box-shadow: 0 6px 10px rgba(0,0,0,0.25);
    color: var(--ink);
    font-family: "Francois One", Arial, sans-serif;
    font-size: 27px;
  }

  /* ---------- services ---------- */
  .services {
    height: 360px;
    display: flex;
    justify-content: space-between;
    padding: 34px 30px 0;
  }
  .service {
    width: 180px;
  }
  .service-title {
    font-family: "Francois One", Arial, sans-serif;
    font-size: 25px;
    line-height: 1.05;
    color: var(--heading-teal);
    text-transform: uppercase;
  }
  .service-visual {
    width: 110px;
    height: 96px;
    margin: 22px auto 16px;
    border-radius: 6px;
  }
  .visual-local { background: #d9dcdf; }
  .visual-national { background: #4a86cf; }
  .visual-ecommerce { background: #cfd4d7; }
  .service-text {
    font-size: 11px;
    line-height: 1.45;
    color: var(--text-grey);
  }
</style>
</head>
<body>
  <div class="page">
    <header class="masthead">
      <div class="topbar">
        <div class="brand"><span class="brand-mark"></span>Marlow Tappers</div>
        <div class="phone">
          <svg width="14" height="14" viewBox="0 0 24 24" aria-hidden="true"><path fill="#ffffff" d="M6.6 10.8a15.1 15.1 0 0 0 6.6 6.6l2.2-2.2a1 1 0 0 1 1-.25 11.4 11.4 0 0 0 3.6.57 1 1 0 0 1 1 1V20a1 1 0 0 1-1 1A17 17 0 0 1 3 4a1 1 0 0 1 1-1h3.5a1 1 0 0 1 1 1c0 1.25.2 2.45.57 3.57a1 1 0 0 1-.25 1z"/></svg>
          Call 1300 48 5527
        </div>
        <nav class="main-nav">
          <a href="#">Home</a>
          <a href="#">Vexora bidlines</a>
          <a href="#">About</a>
          <a href="#">Why choose us?</a>
          <a href="#">Other services</a>
          <a href="#">Contact</a>
        </nav>
      </div>
      <section class="hero">
        <h1 class="hero-title">Want more sales and leads from your bidlines campaign without increasing your budget?</h1>
        <div class="hero-visual" role="img" aria-label="Magnifying glass over web address letters"></div>
      </section>
    </header>

    <section class="health-check">
      <div class="offer">
        <span class="offer-free">FREE</span>
        <span class="offer-name">Bidlines<br>Health Check</span>
      </div>
      <p class="step-title">Step 1: your website</p>
      <input class="url-field" type="text" value="http://" aria-label="Your website address">
      <p class="step-count">STEP 1 OF 3</p>
      <button class="next-button" type="button">NEXT</button>
    </section>

    <section class="services">
      <article class="service">
        <h2 class="service-title">Local<br>Bidlines</h2>
        <div class="service-visual visual-local" role="img" aria-label="Small house illustration"></div>
        <p class="service-text">Our local campaigns target customers searching within your suburb and city, placing your ads in front of nearby buyers ready to call, visit or book with your business today.</p>
      </article>
      <article class="service">
        <h2 class="service-title">National<br>Bidlines</h2>
        <div class="service-visual visual-national" role="img" aria-label="Globe illustration"></div>
        <p class="service-text">National campaigns reach buyers across every state, balancing bids by region and time of day so your budget works harder and each click brings a better chance of a sale.</p>
      </article>
      <article class="service">
        <h2 class="service-title">Ecommerce<br>Bidlines</h2>
        <div class="service-visual visual-ecommerce" role="img" aria-label="Shopping cart with parcels illustration"></div>
        <p class="service-text">Online stores gain shopping ads tuned to margin and stock, with conversion tracking that shows exactly which products and keywords return revenue for every dollar you spend.</p>
      </article>
    </section>
  </div>
</body>
</html>
```